Korvanta

1. We need a four color business card
2. The Front of card needs to include our Logo, Slogan which is "Launching, Expanding & Optimizing Organizations, Individual Name, email, two phone numbers, email, skype address, website address
3. Back of card needs to include the following topics: Start Ups & Business Optimization,Product Acquisition, Destination Product Marketing & Representation,Marketing & Sales, Operations, Training/Education, Digital Marketing, Keynote Addresses/Public Speaking
3. Back of card can not be black as it needs to be a color that people can write on
Industry/Entity Type
Business

```html
<!DOCTYPE html>
<html lang="en">
<head>
<meta charset="utf-8">
<title>Korvanta – Business Card</title>
<link rel="stylesheet" href="https://fonts.googleapis.com/css2?family=Questrial&display=swap">
<style>
  :root {
    --page: #e4e4e4;
    --card-dark: #2b2b2b;
    --card-dark-edge: #1a1a1a;
    --orange: #f26f1d;
    --white: #ffffff;
    --blue: #1f86d6;
    --green: #8dc63f;
    --yellow-light: #ffd814;
    --yellow-deep: #f6a800;
    --navy: #14539a;
    --red: #e0301e;
    --brand: #1f86d6;
  }
  html, body {
    margin: 0;
    padding: 0;
    width: 1200px;
    height: 900px;
    overflow: hidden;
    background: var(--page);
    font-family: "Questrial", "Century Gothic", sans-serif;
  }
  .canvas {
    position: relative;
    width: 1200px;
    height: 900px;
  }
  .card {
    position: absolute;
    left: 250px;
    width: 700px;
    height: 400px;
    box-shadow: 0 10px 30px rgba(0,0,0,0.25);
  }
  .card--front { top: 40px; }
  .card--back  { top: 460px; }
  .card svg { display: block; width: 700px; height: 400px; }
  .brand-name   { fill: var(--brand); font-size: 40px; }
  .slogan       { fill: var(--blue); font-size: 14px; }
  .person-name  { fill: var(--orange); font-size: 36px; }
  .person-email { fill: var(--green); font-size: 30px; }
  .person-phone { fill: var(--blue); font-size: 30px; }
  .bar-label    { fill: var(--white); font-size: 16px; }
  .topic        { font-size: 20px; }
  .topic--navy  { fill: var(--navy); }
  .topic--red   { fill: var(--red); }
</style>
</head>
<body>
<main class="canvas">

  <!-- Front side -->
  <section class="card card--front" aria-label="Card front">
    <svg viewBox="0 0 700 400" xmlns="http://www.w3.org/2000/svg">
      <defs>
        <linearGradient id="front-bg" x1="0" y1="0" x2="1" y2="1">
          <stop offset="0" stop-color="var(--card-dark-edge)"/>
          <stop offset="0.5" stop-color="var(--card-dark)"/>
          <stop offset="1" stop-color="var(--card-dark-edge)"/>
        </linearGradient>
      </defs>
      <rect class="front-base" width="700" height="400" fill="url(#front-bg)"/>
      <polygon class="band-orange" points="0,0 300,0 0,110" fill="var(--orange)"/>
      <polygon class="band-white" points="300,0 620,0 0,230 0,110" fill="var(--white)"/>
      <polygon class="band-blue" points="620,0 650,0 0,241 0,230" fill="var(--blue)"/>
      <polygon class="band-green" points="662,0 690,0 0,256 0,246" fill="var(--green)"/>

      <g class="brand-lockup" transform="translate(30 165) rotate(-20.3)">
        <circle class="brand-dot" cx="16" cy="-13" r="15" fill="var(--orange)"/>
        <text class="brand-name" x="40" y="0">Korvanta</text>
        <text class="slogan" x="6" y="26">Building, Growing &amp; Refining Businesses.</text>
      </g>

      <text class="person-name" x="650" y="195" text-anchor="end">Elena Marsh.</text>
      <text class="person-email" x="650" y="252" text-anchor="end">elena@korvanta.com,</text>
      <text class="person-phone" x="650" y="305" text-anchor="end">555-0142/555-0143.</text>

      <rect class="bar-website" x="0" y="352" width="380" height="48" fill="var(--blue)"/>
      <rect class="bar-accent" x="380" y="352" width="34" height="48" fill="var(--orange)"/>
      <rect class="bar-skype" x="414" y="352" width="286" height="48" fill="var(--green)"/>
      <text class="bar-label" x="110" y="382">website address</text>
      <text class="bar-label" x="500" y="382">skype address</text>
    </svg>
  </section>

  <!-- Back side -->
  <section class="card card--back" aria-label="Card back">
    <svg viewBox="0 0 700 400" xmlns="http://www.w3.org/2000/svg">
      <defs>
        <linearGradient id="back-bg" x1="0" y1="0" x2="1" y2="1">
          <stop offset="0" stop-color="var(--yellow-light)"/>
          <stop offset="1" stop-color="var(--yellow-deep)"/>
        </linearGradient>
      </defs>
      <rect class="back-base" width="700" height="400" fill="url(#back-bg)"/>

      <g class="brand-lockup">
        <circle class="brand-dot" cx="46" cy="48" r="16" fill="var(--orange)"/>
        <text class="brand-name" x="72" y="62">Korvanta</text>
        <text class="slogan" x="30" y="96">Building, Growing &amp; Refining Businesses.</text>
      </g>

      <g class="topic-list" text-anchor="end">
        <text class="topic topic--navy" x="665" y="160">Start Ups &amp; Business Optimization,</text>
        <text class="topic topic--red"  x="665" y="188">Product Acquisition,</text>
        <text class="topic topic--navy" x="665" y="216">Destination Product</text>
        <text class="topic topic--red"  x="665" y="244">Marketing &amp; Representation,</text>
        <text class="topic topic--navy" x="665" y="272">Marketing &amp; Sales, Operations,</text>
        <text class="topic topic--red"  x="665" y="300">Training/Education, Digital Marketing,</text>
        <text class="topic topic--navy" x="665" y="328">Keynote Addresses/Public Speaking</text>
      </g>
    </svg>
  </section>

</main>
</body>
</html>
```